LumaQuill is an online educational platform like Pravento, Skalimo, Tiv...
LumaQuill gives the opportunity to universities to post their courses online and get paid with every purchase.
So we will have courses by category or by university. For now we will start with IT courses (Programming, web development, AI ...).
There will be a login form for clients and also for universities.
every client has his dashboard so he will consult his courses and his progression. Every course has many lessons. and every lesson is composed by videos, QCMs and Quizzes so the client can practice online. At the end of every course, the client will have a final test, if it's passed, he will get certified.
we have uploaded our logos. Designers can choose colors as they want and they have permission to change the logo's color to be adaptable with the website.
We have 3 types of users: Clients, universities and companies.
Universities can post their courses and manage them, can add its students (which are clients) that they will have a discount for their university's courses.
Companies can add their employees and manage them, and they will have a discount (For Entreprise).

Target Market(s)

Everyone who wants to learn something online.

Coding

Coded - Design and coding required

Number of Pages Required

5+ page

Font styles to use
Serif
Sans Serif

Colors

Designer to choose colors to be used in the design.

Requirements
Must have
• A welcome page, to describe who we are.
• we will have courses by category or by university.
• There will be a login form for clients and also for universities.
• every client has his dashboard so he will consult his courses and his progression. Every course has many lessons. and every lesson is composed by videos, QCMs and Quizzes so the client can practice online.
Nice to have
• It would be great if the website is coded with Angular.
• A responsive web design.
• Clients and universities can receive notifications / messages from admins.
• Clients can evaluate the courses.
• Only admins can send messages.
• On the welcome page, we will add our services description which are:
• - We have few courses.
• - Universities certifications.
• - 1-on-1 technical mentor.
• - Real-world projects from industry experts.
• - Flexible learning program.

```html
<!DOCTYPE html>
<html lang="en">
<head>
<meta charset="utf-8">
<title>LumaQuill — Online Education</title>
<link href="https://fonts.googleapis.com/css2?family=Roboto:wght@300;400;500;700&display=swap" rel="stylesheet">
<style>
:root{
  --blue:#1f8ee6;
  --blue-dark:#1572c4;
  --navy:#23364c;
  --ink:#2a3642;
  --muted:#6d7a86;
  --line:#e3e9ef;
  --pale:#eef5fb;
  --white:#ffffff;
  --footer:#f4f7fa;
}
*{box-sizing:border-box;margin:0;padding:0}
html,body{width:1200px;height:3692px;overflow:hidden}
body{font-family:"Roboto",Arial,sans-serif;color:var(--ink);background:var(--white);position:relative}
a{color:inherit;text-decoration:none}

/* header */
.site-header{position:absolute;top:0;left:0;width:1200px;height:72px;background:var(--white);display:flex;align-items:center;padding:0 60px;z-index:5}
.brand{display:flex;align-items:center;gap:10px;font-size:28px;font-weight:500;color:var(--blue)}
.brand-dot{width:18px;height:18px;border-radius:50%;background:var(--blue)}
.main-nav{margin-left:auto;display:flex;align-items:center;gap:30px;font-size:15px;color:var(--ink)}
.main-nav .active{color:var(--blue);border-bottom:2px solid var(--blue);padding-bottom:4px}
.btn-login{background:var(--blue);color:var(--white);padding:9px 26px;border-radius:4px}

/* hero */
.hero{position:absolute;top:72px;left:0;width:1200px;height:640px;background:linear-gradient(100deg,#0d1826 0%,#1b2b3d 40%,#4a4f55 70%,#2a3036 100%)}
.hero-text{position:absolute;left:120px;top:200px;color:var(--white);width:440px}
.hero-text h1{font-size:40px;font-weight:400;line-height:1.15}
.hero-text h1 span{color:var(--white);font-weight:500}
.hero-text p{font-size:14px;line-height:1.5;margin:14px 0 26px;opacity:.85}
.btn-outline{display:inline-block;border:2px solid var(--white);color:var(--white);border-radius:22px;padding:10px 28px;font-size:13px;font-weight:500;letter-spacing:.5px}
.hero-wave{position:absolute;left:0;bottom:-1px;width:1200px;height:50px}
.hero-badge{position:absolute;left:570px;top:676px;width:60px;height:60px;border-radius:50%;background:var(--white);box-shadow:0 4px 14px rgba(0,0,0,.12);display:flex;align-items:center;justify-content:center}
.hero-badge span{width:26px;height:26px;border-radius:50%;background:var(--navy)}

/* section titles */
.section-title{font-size:38px;font-weight:400;color:var(--ink);text-align:center}
.section-lead{font-size:15px;line-height:1.65;color:var(--muted);text-align:center;width:760px;margin:20px auto 0}

/* services */
.services{position:absolute;top:712px;left:0;width:1200px;height:600px;padding-top:64px}
.service-list{display:flex;justify-content:center;gap:40px;margin-top:80px}
.service{width:130px;text-align:center}
.service-icon{width:96px;height:96px;border-radius:50%;background:var(--blue);margin:0 auto 18px;display:flex;align-items:center;justify-content:center;box-shadow:0 0 0 8px #d9ecfb}
.service h3{font-size:15px;font-weight:500;line-height:1.3;color:var(--ink)}

/* courses */
.courses{position:absolute;top:1312px;left:0;width:1200px;height:600px;background:var(--pale);padding-top:60px}
.course-tabs{display:flex;justify-content:center;gap:30px;margin-top:22px;font-size:15px;font-weight:500}
.course-tabs li{list-style:none;padding:7px 18px;border-radius:16px}
.course-tabs .current{background:var(--white);box-shadow:0 2px 8px rgba(0,0,0,.1)}
.course-row{display:flex;justify-content:center;gap:40px;margin-top:40px}
.course-card{width:270px;background:var(--white);border-radius:4px;box-shadow:0 4px 14px rgba(0,0,0,.08);overflow:hidden}
.course-media{height:170px}
.course-media.m1{background:linear-gradient(135deg,#0f2a4a,#3a6fa8,#122033)}
.course-media.m2{background:linear-gradient(135deg,#1a1c20,#8a5a2a,#2b2d30)}
.course-media.m3{background:linear-gradient(135deg,#0b3a5c,#2ca8c9,#072238)}
.course-body{padding:26px 18px 20px;position:relative}
.course-body h4{font-size:17px;font-weight:500;display:flex;justify-content:space-between;align-items:center}
.course-body p{font-size:12px;color:var(--muted);line-height:1.5;margin-top:8px}
.course-pin{position:absolute;top:-22px;left:18px;width:40px;height:40px;border-radius:50%;background:var(--white);box-shadow:0 2px 6px rgba(0,0,0,.15);display:flex;align-items:center;justify-content:center}
.slider-arrow{position:absolute;top:330px}
.slider-arrow.left{left:100px}
.slider-arrow.right{right:100px}

/* who we are */
.who{position:absolute;top:1912px;left:0;width:1200px;height:520px}
.who-photo{position:absolute;inset:0;background:linear-gradient(90deg,#c9d3dc 0%,#e6ecf1 35%,#9aa8b4 60%)}
.who-panel{position:absolute;top:0;right:0;width:680px;height:520px;background:var(--blue);clip-path:polygon(18% 0,100% 0,100% 100%,0 100%)}
.who-text{position:absolute;left:660px;top:88px;width:420px;color:var(--white)}
.who-text h2{font-size:38px;font-weight:400}
.who-text p{font-size:15px;line-height:1.65;margin:18px 0 30px;opacity:.92}

/* testimonials */
.reviews{position:absolute;top:2432px;left:0;width:1200px;height:460px;padding-top:58px}
.review-row{position:relative;height:230px;margin-top:44px}
.review{position:absolute;top:20px;width:330px;padding:22px 26px;background:var(--white);font-size:12px;color:var(--muted);line-height:1.55;opacity:.55}
.review.main{top:0;left:420px;width:360px;opacity:1;box-shadow:0 6px 24px rgba(0,0,0,.12);border-radius:4px}
.review.l{left:20px}
.review.r{left:850px}
.reviewer{display:flex;align-items:center;gap:14px;margin-bottom:14px}
.avatar{width:54px;height:54px;border-radius:50%;background:linear-gradient(135deg,#cfd6dc,#9aa6b0)}
.reviewer strong{display:block;font-size:15px;font-weight:500;color:var(--ink)}
.reviewer span{font-size:12px}
.quote-mark{position:absolute;top:14px;right:20px;width:22px;height:22px;border-radius:50%;background:var(--navy)}
.dots{display:flex;justify-content:center;gap:10px;margin-top:16px}
.dots i{width:10px;height:10px;border-radius:50%;border:1.5px solid var(--blue)}
.dots i.on{background:var(--blue)}

/* cta */
.cta{position:absolute;top:2892px;left:0;width:1200px;height:420px;background:linear-gradient(180deg,#2e3d4e,#1b2836 60%,#22303e);text-align:center;color:var(--white);padding-top:130px}
.cta h2{font-size:38px;font-weight:400}
.cta p{font-size:15px;line-height:1.6;width:620px;margin:16px auto 26px;opacity:.85}
.btn-white{display:inline-block;background:var(--white);color:var(--blue);border-radius:22px;padding:12px 30px;font-size:13px;font-weight:700;letter-spacing:.5px}

/* footer */
.site-footer{position:absolute;top:3312px;left:0;width:1200px;height:380px;background:var(--footer)}
.footer-brand{position:absolute;left:110px;top:60px}
.footer-brand .brand{font-size:34px}
.footer-cols{position:absolute;left:410px;top:56px;display:flex;gap:70px}
.footer-col h5{font-size:13px;font-weight:700;letter-spacing:.8px;color:var(--ink);margin-bottom:12px}
.footer-col li{list-style:none;font-size:12px;color:var(--muted);line-height:1.9}
.contact-item{display:flex;gap:10px;align-items:flex-start;font-size:12px;color:var(--muted);line-height:1.5;margin-bottom:14px}
.contact-item b{display:block;color:var(--ink);font-weight:500}
.copyright{position:absolute;left:0;bottom:0;width:1200px;height:52px;border-top:1px solid var(--line);text-align:center;font-size:11px;color:var(--muted);line-height:52px}
</style>
</head>
<body>

<header class="site-header">
  <a class="brand" href="#"><span class="brand-dot"></span>LumaQuill</a>
  <nav class="main-nav">
    <a class="active" href="#">Courses</a>
    <a href="#">Who we are</a>
    <a href="#">Programs</a>
    <a href="#">Why Us</a>
    <a href="#">Career</a>
    <a href="#">Sign in</a>
    <a class="btn-login" href="#">Log in</a>
  </nav>
</header>

<section class="hero" role="img" aria-label="Two students studying together at a laptop">
  <div class="hero-text">
    <h1>Best Online Education<br><span>With LumaQuill</span></h1>
    <p>Nunc tempus felis vitae urna Vivamus porttitor neque et volutpat rutrum purus nisi eleifend libero a tempus.</p>
    <a class="btn-outline" href="#">GET STARTED</a>
  </div>
  <svg class="hero-wave" viewBox="0 0 1200 50" preserveAspectRatio="none"><path d="M0 50 L0 20 Q600 60 1200 20 L1200 50 Z" fill="#fff"/></svg>
</section>
<div class="hero-badge"><span></span></div>

<section class="services">
  <h2 class="section-title">Our Services</h2>
  <p class="section-lead">Nunc tempus felis vitae urna Vivamus porttitor neque et volutpat rutrum purus nisi eleifend libero a tempus feugiat felis Morbi diam mauris viverra in gravida eu mattis in ante Morbi eget arcu Morbi porta libero id ullamcorper nonummy nibh ligula pulvinar metus.</p>
  <div class="service-list">
    <div class="service">
      <div class="service-icon"><svg width="44" height="44" viewBox="0 0 44 44" fill="none" stroke="#fff" stroke-width="2.5"><circle cx="22" cy="22" r="16"/><path d="M6 22h32M22 6c6 6 6 26 0 32M22 6c-6 6-6 26 0 32"/></svg></div>
      <h3>We have few courses</h3>
    </div>
    <div class="service">
      <div class="service-icon"><svg width="44" height="44" viewBox="0 0 44 44" fill="none" stroke="#fff" stroke-width="2.5"><rect x="9" y="6" width="26" height="32" rx="2"/><path d="M15 15h14M15 21h14M15 27h8"/></svg></div>
      <h3>Universities Certifications</h3>
    </div>
    <div class="service">
      <div class="service-icon"><svg width="44" height="44" viewBox="0 0 44 44" fill="none" stroke="#fff" stroke-width="2.5"><rect x="6" y="9" width="32" height="22" rx="2"/><path d="M16 37h12M22 31v6"/><circle cx="22" cy="19" r="4"/></svg></div>
      <h3>1-on-1 Technical Mentor</h3>
    </div>
    <div class="service">
      <div class="service-icon"><svg width="44" height="44" viewBox="0 0 44 44" fill="none" stroke="#fff" stroke-width="2.5"><rect x="7" y="12" width="30" height="22" rx="2"/><path d="M16 12V8h12v4M7 21h30"/></svg></div>
      <h3>Real-world projects from industry experts</h3>
    </div>
    <div class="service">
      <div class="service-icon"><svg width="44" height="44" viewBox="0 0 44 44" fill="none" stroke="#fff" stroke-width="2.5"><rect x="7" y="9" width="30" height="28" rx="2"/><path d="M7 17h30M15 5v8M29 5v8M15 25l5 5 9-9"/></svg></div>
      <h3>Flexible learning program</h3>
    </div>
  </div>
</section>

<section class="courses">
  <h2 class="section-title">Our Courses</h2>
  <ul class="course-tabs">
    <li class="current">Data Science</li>
    <li>Artificial Intelligence</li>
    <li>Programming</li>
    <li>Cloud Computing</li>
    <li>Autonomous</li>
  </ul>
  <svg class="slider-arrow left" width="20" height="36" viewBox="0 0 20 36"><path d="M17 2 3 18l14 16" fill="none" stroke="#8fa0ae" stroke-width="2"/></svg>
  <svg class="slider-arrow right" width="20" height="36" viewBox="0 0 20 36"><path d="M3 2l14 16L3 34" fill="none" stroke="#8fa0ae" stroke-width="2"/></svg>
  <div class="course-row">
    <article class="course-card">
      <div class="course-media m1" role="img" aria-label="Course cover showing data charts on a screen"></div>
      <div class="course-body">
        <span class="course-pin"><svg width="18" height="18" viewBox="0 0 18 18" fill="none" stroke="#1f8ee6" stroke-width="2"><circle cx="9" cy="7" r="4"/><path d="M7 11v4h4v-4"/></svg></span>
        <h4>Courses Title here <svg width="18" height="12" viewBox="0 0 18 12"><path d="M0 6h16M11 1l5 5-5 5" fill="none" stroke="#1f8ee6" stroke-width="2"/></svg></h4>
        <p>Fusce tellus Sed metus augue cons alto at vehicula ut pulvinar.</p>
      </div>
    </article>
    <article class="course-card">
      <div class="course-media m2" role="img" aria-label="Course cover showing a circuit board"></div>
      <div class="course-body">
        <span class="course-pin"><svg width="18" height="18" viewBox="0 0 18 18" fill="none" stroke="#1f8ee6" stroke-width="2"><circle cx="9" cy="7" r="4"/><path d="M7 11v4h4v-4"/></svg></span>
        <h4>Courses Title here <svg width="18" height="12" viewBox="0 0 18 12"><path d="M0 6h16M11 1l5 5-5 5" fill="none" stroke="#1f8ee6" stroke-width="2"/></svg></h4>
        <p>Fusce tellus Sed metus augue cons alto at vehicula ut pulvinar.</p>
      </div>
    </article>
    <article class="course-card">
      <div class="course-media m3" role="img" aria-label="Course cover showing a glowing digital network"></div>
      <div class="course-body">
        <span class="course-pin"><svg width="18" height="18" viewBox="0 0 18 18" fill="none" stroke="#1f8ee6" stroke-width="2"><circle cx="9" cy="7" r="4"/><path d="M7 11v4h4v-4"/></svg></span>
        <h4>Courses Title here <svg width="18" height="12" viewBox="0 0 18 12"><path d="M0 6h16M11 1l5 5-5 5" fill="none" stroke="#1f8ee6" stroke-width="2"/></svg></h4>
        <p>Fusce tellus Sed metus augue cons alto at vehicula ut pulvinar.</p>
      </div>
    </article>
  </div>
</section>

<section class="who">
  <div class="who-photo" role="img" aria-label="Student working on a laptop at a desk"></div>
  <div class="who-panel"></div>
  <div class="who-text">
    <h2>Who We Are</h2>
    <p>Nunc tempus felis vitae urna Vivamus porttitor neque et volutpat rutrum purus nisi eleifend libero a tempus feugiat felis Morbi diam mauris viverra in gravida eu mattis in ante Morbi eget arcu Morbi porta libero id ullamcorper nonummy nibh ligula pulvinar metus.</p>
    <a class="btn-outline" href="#">LEARN MORE</a>
  </div>
</section>

<section class="reviews">
  <h2 class="section-title">What People Says</h2>
  <div class="review-row">
    <div class="review l">
      <div class="reviewer"><span class="avatar" role="img" aria-label="Reviewer portrait"></span><div><strong>Dana Morell</strong><span>Company Name</span></div></div>
      Curabitur iaculis tempus eros Curabitur nisi et amet magna malesuada ultrices id nisi erat fermentum vel congue et euismod in elit.
    </div>
    <div class="review main">
      <span class="quote-mark"></span>
      <div class="reviewer"><span class="avatar" role="img" aria-label="Reviewer portrait"></span><div><strong>Dana Morell</strong><span>Company Name</span></div></div>
      Curabitur iaculis tempus eros Curabitur nisi et amet magna malesuada ultrices id nisi erat fermentum vel congue et euismod in elit.
    </div>
    <div class="review r">
      <div class="reviewer"><span class="avatar" role="img" aria-label="Reviewer portrait"></span><div><strong>Lena Ortiz</strong><span>Company Name</span></div></div>
      Curabitur iaculis tempus eros Curabitur nisi et amet magna malesuada ultrices id nisi erat fermentum vel congue et euismod in elit.
    </div>
  </div>
  <div class="dots"><i></i><i class="on"></i><i></i></div>
</section>

<section class="cta" role="img" aria-label="Dim classroom backdrop behind the call to action">
  <h2>Are Your Ready to Start?</h2>
  <p>Nunc tempus felis vitae urna Vivamus porttitor neque et volutpat rutrum purus nisi eleifend libero a tempus feugiat felis Morbi diam.</p>
  <a class="btn-white" href="#">GET STARTED</a>
</section>

<footer class="site-footer">
  <div class="footer-brand"><a class="brand" href="#"><span class="brand-dot"></span>LumaQuill</a></div>
  <div class="footer-cols">
    <div class="footer-col"><h5>COMPANY</h5><ul><li>Home</li><li>About us</li><li>Why Choose Us</li><li>Courses</li><li>Get Started</li><li>Contact</li></ul></div>
    <div class="footer-col"><h5>COURSES</h5><ul><li>Pellentesque</li><li>Faucibus Ut</li><li>Accumsan nisl</li><li>Enim vestibulum</li><li>Non fermentum</li><li>Nec laoreet</li></ul></div>
    <div class="footer-col"><h5>RESOURCES</h5><ul><li>Support</li><li>Sitemap</li><li>Career</li><li>FAQ</li><li>Contact</li></ul></div>
    <div class="footer-col"><h5>QUESTIONS</h5>
      <div class="contact-item"><svg width="16" height="16" viewBox="0 0 16 16"><path d="M3 1h3l1 4-2 1a8 8 0 0 0 5 5l1-2 4 1v3c0 1-1 2-2 2A13 13 0 0 1 1 3c0-1 1-2 2-2z" fill="#1f8ee6"/></svg><div><b>Call Us Now</b>(312) 555 0187</div></div>
      <div class="contact-item"><svg width="16" height="16" viewBox="0 0 16 16"><rect x="1" y="3" width="14" height="10" rx="1" fill="none" stroke="#1f8ee6" stroke-width="1.6"/><path d="M1 4l7 5 7-5" fill="none" stroke="#1f8ee6" stroke-width="1.6"/></svg><div><b>Email Us</b>hello@lumaquill.edu</div></div>
    </div>
  </div>
  <div class="copyright">Copyright © 2019 All right reserved</div>
</footer>

</body>
</html>
```